New Zealand Marlborough Sauvignon Blanc wine packaging design

We need packaging design for our new wine brand, Dunmore Hale. The wine is a New Zealand Marlborough Sauvignon Blanc. We would like the packaging will portray elegance and style with an understated label. We are looking for a label that portrays the elegance of the French Riviera. The label should be round or pill shaped.
Updates

Industry/Entity Type

Wine

Font styles to use
Serif
Sans Serif

Requirements
Must have
• The words in order of importance: Dunmore Hale, Sauvignon Blanc, Marlborough, New Zealand. It should be fit to the bottle posted in the links
Nice to have
• a pill shape or circular shape
Should not have
• Illustrations of wine bottles, wine glasses, or grapes

```html
<!DOCTYPE html>
<html lang="en">
<head>
<meta charset="utf-8">
<title>Dunmore Hale — Marlborough Sauvignon Blanc Label</title>
<link rel="stylesheet" href="https://fonts.googleapis.com/css2?family=Rye&family=Montserrat:wght@500;700&family=Federo&family=EB+Garamond&family=Playfair+Display:ital@1&display=swap">
<style>
  :root {
    --cream-bg: #fef7d3;
    --ink: #000000;
    --paper: #ffffff;
    --sketch-light: #ecebe4;
    --forest: #383d1c;
    --olive: #9b9641;
    --gold-light: #fff6c4;
    --gold-mid: #e8c548;
    --gold-deep: #c8971a;
    --label-cream: #fbf4cf;
    --stage-glow: #6a6932;
    --stage-dark: #1c1b13;
    --band-green: #404b3c;
    --band-line: #b9b9a8;
    --band-text: #e9e9e1;
  }
  * { margin: 0; padding: 0; box-sizing: border-box; }
  html, body { width: 773px; height: 1200px; overflow: hidden; }
  body { position: relative; background: var(--stage-dark); }

  .presentation-top {
    position: absolute; left: 0; top: 0; width: 773px; height: 352px;
    background: var(--cream-bg);
  }
  .presentation-stage {
    position: absolute; left: 0; top: 352px; width: 773px; height: 848px;
    background: radial-gradient(ellipse 420px 460px at 330px 470px, var(--stage-glow) 0%, #45431f 45%, var(--stage-dark) 100%);
  }

  .label { position: absolute; display: block; }
  .label--mono { left: 156px; top: 68px; width: 190px; height: 236px; }
  .label--gold { left: 425px; top: 68px; width: 190px; height: 236px; }
  .label--feature { left: 79px; top: 108px; width: 160px; height: 199px; }
  .presentation-stage .label--feature { left: 316px; top: 460px; }

  .brand-arc { font-family: "Rye", serif; font-size: 17px; letter-spacing: 0.5px; }
  .region { font-family: "Montserrat", sans-serif; font-weight: 700; font-size: 14.5px; letter-spacing: 0.4px; }
  .variety { font-family: "Federo", sans-serif; font-size: 13px; letter-spacing: 0.4px; }
  .vintage { font-family: "EB Garamond", serif; font-size: 13px; }
  .origin-arc { font-family: "Montserrat", sans-serif; font-weight: 500; font-size: 10.5px; letter-spacing: 0.2px; }

  .variety-band {
    position: absolute; left: 285px; top: 663px; width: 218px; height: 85px;
    background: var(--band-green);
    border-top: 1px solid var(--band-line);
    border-bottom: 1px solid var(--band-line);
    text-align: center; color: var(--band-text);
  }
  .variety-band::before, .variety-band::after {
    content: ""; position: absolute; left: 0; right: 0; height: 1px; background: var(--band-line); opacity: .6;
  }
  .variety-band::before { top: 5px; }
  .variety-band::after { bottom: 5px; }
  .variety-band__name {
    margin-top: 22px;
    font-family: "Playfair Display", serif; font-style: italic; font-size: 17px;
  }
  .variety-band__region {
    margin-top: 4px;
    font-family: "Montserrat", sans-serif; font-weight: 500; font-size: 7.5px; letter-spacing: 2.6px;
  }
</style>
</head>
<body>

<section class="presentation-top">
  <!-- Single-colour version -->
  <svg class="label label--mono" viewBox="0 0 190 236" aria-label="Dunmore Hale label, black and white">
    <defs>
      <clipPath id="mono-inner"><rect x="9" y="9" width="172" height="218" rx="84"/></clipPath>
      <path id="mono-top-arc" d="M30 92 A65 65 0 0 1 160 92"/>
      <path id="mono-bottom-arc" d="M41 164 A54 54 0 0 0 149 164"/>
    </defs>
    <rect x="4" y="4" width="182" height="228" rx="89" fill="var(--paper)" stroke="var(--ink)" stroke-width="8"/>
    <g clip-path="url(#mono-inner)">
      <rect x="9" y="9" width="172" height="218" fill="var(--sketch-light)" role="img" aria-label="Fine-line sketch of a hillside above a coastal village"/>
      <path d="M17 92 A78 78 0 0 1 173 92 L153 92 A58 58 0 0 0 37 92 Z" fill="var(--paper)" stroke="var(--ink)" stroke-width="1.2"/>
      <rect x="0" y="106" width="190" height="51" fill="var(--ink)"/>
      <path d="M33 164 A62 62 0 0 0 157 164 L139 164 A44 44 0 0 1 51 164 Z" fill="var(--paper)" stroke="var(--ink)" stroke-width="1.2"/>
    </g>
    <text class="brand-arc" fill="var(--paper)" stroke="var(--ink)" stroke-width="1"><textPath href="#mono-top-arc" startOffset="50%" text-anchor="middle">DUNMORE HALE</textPath></text>
    <text class="region" x="95" y="127" text-anchor="middle" fill="var(--paper)">MARLBOROUGH</text>
    <text class="variety" x="95" y="147" text-anchor="middle" fill="var(--paper)">SAUVIGNON BLANC</text>
    <text class="vintage" x="95" y="179" text-anchor="middle" fill="var(--ink)">2023</text>
    <text class="origin-arc" fill="var(--ink)"><textPath href="#mono-bottom-arc" startOffset="50%" text-anchor="middle" dominant-baseline="central">WINE OF NEW ZEALAND</textPath></text>
  </svg>

  <!-- Gold foil version -->
  <svg class="label label--gold" viewBox="0 0 190 236" aria-label="Dunmore Hale label, gold">
    <defs>
      <linearGradient id="gold-ring" x1="0" y1="0" x2="1" y2="0">
        <stop offset="0" stop-color="var(--gold-deep)"/>
        <stop offset="0.2" stop-color="var(--gold-light)"/>
        <stop offset="0.55" stop-color="var(--gold-mid)"/>
        <stop offset="0.8" stop-color="var(--gold-light)"/>
        <stop offset="1" stop-color="var(--gold-deep)"/>
      </linearGradient>
      <linearGradient id="gold-band" x1="0" y1="0" x2="1" y2="0">
        <stop offset="0" stop-color="var(--gold-mid)"/>
        <stop offset="0.35" stop-color="var(--gold-light)"/>
        <stop offset="0.75" stop-color="var(--gold-light)"/>
        <stop offset="1" stop-color="var(--gold-mid)"/>
      </linearGradient>
      <clipPath id="gold-inner"><rect x="9" y="9" width="172" height="218" rx="84"/></clipPath>
      <path id="gold-top-arc" d="M30 92 A65 65 0 0 1 160 92"/>
      <path id="gold-bottom-arc" d="M41 164 A54 54 0 0 0 149 164"/>
      <symbol id="gold-label-art" viewBox="0 0 190 236">
        <rect x="0" y="0" width="190" height="236" rx="95" fill="url(#gold-ring)"/>
        <g clip-path="url(#gold-inner)">
          <rect x="9" y="9" width="172" height="218" fill="var(--label-cream)" role="img" aria-label="Fine-line sketch of a hillside above a coastal village"/>
          <path d="M17 92 A78 78 0 0 1 173 92 L153 92 A58 58 0 0 0 37 92 Z" fill="var(--forest)"/>
          <rect x="0" y="106" width="190" height="51" fill="url(#gold-band)"/>
          <path d="M33 164 A62 62 0 0 0 157 164 L139 164 A44 44 0 0 1 51 164 Z" fill="var(--forest)"/>
          <path d="M51 164 A44 44 0 0 0 139 164 Z" fill="var(--olive)"/>
        </g>
        <text class="brand-arc" fill="var(--label-cream)"><textPath href="#gold-top-arc" startOffset="50%" text-anchor="middle">DUNMORE HALE</textPath></text>
        <text class="region" x="95" y="127" text-anchor="middle" fill="var(--forest)">MARLBOROUGH</text>
        <text class="variety" x="95" y="147" text-anchor="middle" fill="var(--forest)">SAUVIGNON BLANC</text>
        <text class="vintage" x="95" y="179" text-anchor="middle" fill="var(--forest)">2023</text>
        <text class="origin-arc" fill="var(--label-cream)"><textPath href="#gold-bottom-arc" startOffset="50%" text-anchor="middle" dominant-baseline="central">WINE OF NEW ZEALAND</textPath></text>
      </symbol>
    </defs>
    <use href="#gold-label-art" x="0" y="0" width="190" height="236"/>
  </svg>
</section>

<section class="presentation-stage">
  <svg class="label label--feature" viewBox="0 0 190 236" aria-label="Dunmore Hale label, gold, front view">
    <use href="#gold-label-art" x="0" y="0" width="190" height="236"/>
  </svg>
  <div class="variety-band" style="top:311px;">
    <p class="variety-band__name">Sauvignon Blanc</p>
    <p class="variety-band__region">MARLBOROUGH</p>
  </div>
</section>

</body>
</html>
```